Event Ticketing homepage design

This contest is for an event ticketing homepage to be based on the script - http://www.gatherpass-tix.com/demo5/index.php.

Similar ticketing systems for which ideas can be generated are: showlark dotcom, gotseats dotcom and happenry dotcom.

The homepage these will be based on this design: http://www.vorbix.com/nl/home.html

Features that the design should have include:

1. All positions shown in the demo
2. Top navigation menu: Left hand side - Chatterly and Peepsy icons, Add event. Right hand side – Sign Up, Sign In, Forgot Password
3. Featured events with “buy now” buttons
4. Search function
5. Chatterly connect (near login)
6. Create event (see showlark dotcom)
7. Most viewed (see gotseats dotcom)
8. Best sellers (see gotseats dotcom)
9. Main Menu navigation buttons: Home,
10. About us, How to advertise, Policies, How to purchase, Terms and Conditions, FAQs, Privacy Policy, Contact Us, Copyright in the footer
11. Hot spots (see happenry dotcom)

I will provide the background image to top designers before choosing a finalist
Final design should have high quality PSD files.

Reason: Due to request from Lou, i have decided to add 4 more days

Here is the new inspiration http://brivontechlabs.com/devpro/DuskScene/index.html

Thanks for the designs. We'll be giving feedback to all by the end of today (US eastern time)

Thanks for all designs submitted. As the contest is only one or several designs can be considered and so if I don't leave feedback know that it was not shortlisted to be among the finalists.

Reason: For changes

```html
<!DOCTYPE html>
<html lang="en">
<head>
<meta charset="utf-8">
<title>Lumora – Event Ticketing</title>
<link href="https://fonts.googleapis.com/css2?family=Arimo:wght@400;700&family=Bebas+Neue&family=Exo+2:ital,wght@0,700;1,600&family=Open+Sans:wght@400&display=swap" rel="stylesheet">
<style>
:root{
  --bg:#000;
  --band:#161616;
  --panel:#2b2b2b;
  --row-line:#3d3d3d;
  --white:#fff;
  --muted:#8a8a8a;
  --link:#9a9a9a;
  --orange:#f7a21b;
  --orange-dark:#e8820c;
  --gold:#c98a1a;
  --pink:#e268c4;
  --footer:#1e1e1e;
}
*{margin:0;padding:0;box-sizing:border-box}
html,body{width:1054px;height:1200px;overflow:hidden;background:var(--bg);font-family:"Arimo",Arial,sans-serif;color:var(--white)}
.page{position:relative;width:1054px;height:1200px}
.abs{position:absolute}

/* hero */
.hero{left:0;top:0;width:1054px;height:355px;background:linear-gradient(180deg,#050505 0%,#0c0710 40%,#1a0c1e 70%,#0a0608 100%)}
.hero-lights{left:0;top:130px;width:700px;height:225px;background:radial-gradient(ellipse at 30% 60%,rgba(200,60,160,.45),transparent 60%),radial-gradient(ellipse at 75% 40%,rgba(60,120,180,.35),transparent 55%)}
.hero-photo{left:590px;top:0;width:464px;height:355px;background:radial-gradient(ellipse at 55% 45%,#6a4a52 0%,#3a2230 45%,#1c0e18 75%,#0c070b 100%)}
.logo{left:92px;top:12px;font:700 58px/1 "Exo 2",sans-serif;color:var(--pink);letter-spacing:3px}
.account{right:24px;top:13px;font-size:13px;color:var(--orange)}
.account span{color:var(--orange);margin:0 5px}
.tagline{left:102px;top:172px;font:italic 600 28px/1 "Exo 2",sans-serif;letter-spacing:2px}
.intro{left:102px;top:236px;width:520px;font:17px/1.1 "Open Sans",sans-serif}
.btn-create{left:428px;top:289px;width:182px;height:42px;background:linear-gradient(#fdb12a,var(--orange-dark));border-radius:3px;font:20px/42px Georgia,serif;text-align:center;color:var(--white)}

/* nav */
.main-nav{left:0;top:355px;width:1054px;height:65px;background:linear-gradient(#1e1e1e,#0e0e0e);display:flex;padding-left:97px}
.main-nav a{display:block;height:65px;line-height:66px;text-align:center;font:22px/66px "Bebas Neue",sans-serif;color:#ddd;text-decoration:none;border-right:1px solid #2c2c2c;letter-spacing:.5px}
.main-nav a.active{background:linear-gradient(#f0f0f0,#8a8a8a 60%,#5a5a5a);color:#111}

/* featured */
.search-band{left:0;top:420px;width:1054px;height:60px;background:var(--band)}
.section-title{font:22px/1 "Open Sans",sans-serif;color:var(--white)}
.search-label{left:741px;top:437px;font-size:11px}
.search-input{left:785px;top:429px;width:225px;height:27px;background:#000;border:1px solid #333}
.search-go{left:1017px;top:430px;width:23px;height:23px;background:var(--orange);font-size:12px;line-height:23px;text-align:center}
.featured{left:0;top:480px;width:1054px;height:288px;background:#000}
.event-thumb{width:205px;height:106px;border:1px solid #2c2c2c;padding:4px;background:#0a0a0a}
.event-thumb div{width:100%;height:100%}
.tone-pink{background:linear-gradient(120deg,#d86aa0,#f2a3c8 45%,#5fb5e8)}
.tone-green{background:linear-gradient(120deg,#2a1a1c,#6a3a3a 50%,#6ad040)}
.event-link{width:240px;font-size:11px;line-height:16px;color:var(--link);text-decoration:underline}
.event-desc{width:250px;font-size:9px;line-height:16px;text-transform:uppercase;letter-spacing:.2px}
.view-more{font-size:9px;color:var(--gold);text-decoration:underline}

/* lists */
.lists{left:0;top:768px;width:1054px;height:345px;background:var(--band)}
.list-panel{background:var(--panel)}
.list-row{position:absolute;left:0;width:100%;height:88px;border-bottom:2px solid var(--row-line)}
.list-row:last-child{border-bottom:none}
.ticket-thumb{position:absolute;left:7px;top:16px;width:122px;height:57px;border:2px solid #bbb}
.poster-purple{background:linear-gradient(135deg,#3a2a6a,#b9a8e0 50%,#5a4a9a)}
.poster-spring{background:linear-gradient(135deg,#e0c070,#fff0b0 50%,#50a8c8)}
.ticket-info{position:absolute;left:144px;top:13px;font-size:12px;line-height:18px;letter-spacing:.3px}
.btn-buy{position:absolute;left:143px;top:49px;width:111px;height:25px;border-radius:3px;background:linear-gradient(#fdc13a,var(--orange-dark));font:italic 700 15px/25px "Arimo",sans-serif;color:#222;text-align:center}
.hot-panel{left:774px;top:807px;width:267px;height:269px;background:#000}
.hot-photo{left:7px;top:15px;width:248px;height:136px;border:3px solid #888;background:linear-gradient(135deg,#3a1230,#d0306a 45%,#601a6a 70%,#1a0a2a)}
.hot-text{left:19px;top:166px;width:240px;font-size:10px;line-height:16px;color:var(--muted)}
.hot-more{left:19px;top:242px}

/* footer */
.footer{left:0;top:1113px;width:1054px;height:87px;background:var(--footer);border-top:2px solid #333}
.social{left:50px;top:30px;display:flex;gap:16px}
.social span{display:flex;align-items:center;gap:5px;font-size:11px;color:#ccc}
.social i{display:block;width:22px;height:22px;border-radius:4px;background:#5a8fc0}
.footer-links{right:27px;top:20px;font-size:12px;text-align:right}
.copyright{right:27px;top:50px;font-size:12px}
</style>
</head>
<body>
<div class="page">

  <header>
    <div class="abs hero"></div>
    <div class="abs hero-lights" role="img" aria-label="Glowing disco light wall in pink and blue"></div>
    <div class="abs hero-photo" role="img" aria-label="Dancer in a grey fedora under stage lights"></div>
    <div class="abs logo">LUMORA</div>
    <div class="abs account">login<span>|</span>Sign Up</div>
    <h1 class="abs tagline">MAKE YOUR EVENT A SUCCESS</h1>
    <p class="abs intro">Lumora empowers you with simple but powerful tools to manage, promote, and sell out your event. It's free to sign up and get started.</p>
    <div class="abs btn-create">Create an event</div>
  </header>

  <nav class="abs main-nav">
    <a class="active" style="width:121px">MAIN</a>
    <a style="width:114px">ABOUT US</a>
    <a style="width:165px">HOW TO ADVERTISE</a>
    <a style="width:104px">POLICIES</a>
    <a style="width:173px">HOW TO PURCHASE</a>
    <a style="width:166px">CONTACT US</a>
  </nav>

  <div class="abs search-band"></div>
  <h2 class="abs section-title" style="left:48px;top:448px">Featured events</h2>
  <div class="abs search-label">Search</div>
  <div class="abs search-input"></div>
  <div class="abs search-go">Go</div>

  <section class="abs featured"></section>

  <div class="abs event-thumb" style="left:45px;top:493px"><div class="tone-pink" role="img" aria-label="Featured party event photo"></div></div>
  <a class="abs event-link" style="left:267px;top:494px">Nemo enim ipsam voluptatem quia voluptas sit odit aut fugit, sed quia consequuntur.</a>
  <p class="abs event-desc" style="left:267px;top:538px">Aenean nonummy hendrerit mauris phasellus fuscesuscipit varius micum sociis natoque magnis dis parturient montes, nascetur nulla dui. Fusce feugiat malesuada odio.</p>
  <div class="abs event-thumb" style="left:45px;top:614px"><div class="tone-green" role="img" aria-label="Featured club night photo"></div></div>
  <a class="abs event-link" style="left:267px;top:615px">Nemo enim ipsam voluptatem quia voluptas sit odit aut fugit, sed quia consequuntur.</a>
  <p class="abs event-desc" style="left:267px;top:659px">Mauris phasellus porta<br>varius micum sociis natoque penatibus et magnis dis parturient montes, nascetur nulla dui. Fusce feugiat malesuada odio.</p>
  <a class="abs view-more" style="left:45px;top:737px">VIEW MORE</a>

  <div class="abs event-thumb" style="left:550px;top:493px"><div class="tone-pink" role="img" aria-label="Featured party event photo"></div></div>
  <a class="abs event-link" style="left:772px;top:494px">Nemo enim ipsam voluptatem quia voluptas sit odit aut fugit, sed quia consequuntur.</a>
  <p class="abs event-desc" style="left:772px;top:538px">Aenean nonummy hendrerit mauris phasellus fuscesuscipit varius micum sociis natoque magnis dis parturient montes, nascetur nulla dui. Fusce feugiat malesuada odio.</p>
  <div class="abs event-thumb" style="left:550px;top:614px"><div class="tone-green" role="img" aria-label="Featured club night photo"></div></div>
  <a class="abs event-link" style="left:772px;top:615px">Nemo enim ipsam voluptatem quia voluptas sit odit aut fugit, sed quia consequuntur.</a>
  <p class="abs event-desc" style="left:772px;top:659px">Mauris phasellus porta<br>varius micum sociis natoque penatibus et magnis dis parturient montes, nascetur nulla dui. Fusce feugiat malesuada odio.</p>
  <a class="abs view-more" style="left:550px;top:737px">VIEW MORE</a>

  <section class="abs lists"></section>
  <h2 class="abs section-title" style="left:43px;top:777px;font-size:20px">Best Sellers</h2>
  <h2 class="abs section-title" style="left:408px;top:777px;font-size:20px">Most Viewd Events</h2>
  <h2 class="abs section-title" style="left:773px;top:777px;font-size:20px">Hot Spots</h2>

  <div class="abs list-panel" style="left:38px;top:807px;width:361px;height:269px">
    <div class="list-row" style="top:0"><div class="ticket-thumb poster-purple" role="img" aria-label="Frosh week party poster"></div><div class="ticket-info">VEYRAC FROSH WEEK 2011<br>HARBOR MUSIC HALL | Elmridge, ON</div><div class="btn-buy">Buy Now</div></div>
    <div class="list-row" style="top:89px"><div class="ticket-thumb poster-purple" role="img" aria-label="Frosh week party poster"></div><div class="ticket-info">VEYRAC FROSH WEEK 2011<br>HARBOR MUSIC HALL | Elmridge, ON</div><div class="btn-buy">Buy Now</div></div>
    <div class="list-row" style="top:179px"><div class="ticket-thumb poster-purple" role="img" aria-label="Frosh week party poster"></div><div class="ticket-info">VEYRAC FROSH WEEK 2011<br>HARBOR MUSIC HALL | Elmridge, ON</div><div class="btn-buy">Buy Now</div></div>
  </div>

  <div class="abs list-panel" style="left:406px;top:807px;width:361px;height:269px">
    <div class="list-row" style="top:0"><div class="ticket-thumb poster-spring" role="img" aria-label="Spring break party poster"></div><div class="ticket-info">VEYRAC FROSH WEEK 2011<br>HARBOR MUSIC HALL | Elmridge, ON</div><div class="btn-buy">Buy Now</div></div>
    <div class="list-row" style="top:89px"><div class="ticket-thumb poster-purple" role="img" aria-label="Frosh week party poster"></div><div class="ticket-info">VEYRAC FROSH WEEK 2011<br>HARBOR MUSIC HALL | Elmridge, ON</div><div class="btn-buy">Buy Now</div></div>
    <div class="list-row" style="top:179px"><div class="ticket-thumb poster-spring" role="img" aria-label="Spring break party poster"></div><div class="ticket-info">VEYRAC FROSH WEEK 2011<br>HARBOR MUSIC HALL | Elmridge, ON</div><div class="btn-buy">Buy Now</div></div>
  </div>

  <div class="abs hot-panel">
    <div class="abs hot-photo" role="img" aria-label="Crowded nightclub dance floor under pink lights"></div>
    <p class="abs hot-text">Perspiciatis unde omnis iste natus error sit voluptatem accusantium doloremque laudantium, totam rem aperiam, eaque ipsa quae ab illo inventore veritatis et quasi architecto...</p>
    <a class="abs view-more hot-more">READ MORE</a>
  </div>

  <footer class="abs footer">
    <div class="abs social">
      <span><i></i>Peepsy</span>
      <span><i style="background:#3b5a9a"></i>Chatterly</span>
      <span><i style="background:#2a78b0"></i>Linkora</span>
      <span><i style="background:#f08a20"></i>RSS</span>
      <span><i style="background:#ddd"></i>Pixbin</span>
      <span><i style="background:#3a5fa8"></i>Spacely</span>
      <span><i style="background:#3aa040"></i>Stumblo</span>
    </div>
    <div class="abs footer-links">Terms and Conditions | FAQs | Privacy Policy | Contact Us</div>
    <div class="abs copyright">Copyright @Lumora 2011. All Rights Reserved.</div>
  </footer>

</div>
</body>
</html>
```